Lawn care business card

I am looking for a quality designed personal business card to represent the quality and elegant nature of our company. We separate ourselves in our market by the aesthetic value of our work, so I am looking for marketing material that does the same. We target our marketing high end customers, and we try to avoid price shoppers. I am open to all design options, so long as they are in line with our companies values.

We are tend to go with a retro look on everything from our logo and print material, to our uniforms. We like to portray and "old fashion" set of core values, with a modern elegance. So a wild and crazy look is out of the question.

Things I'd like on the card:
1.) Logo
2.) Phone number: (816) 555-0193
3.) Website: Verdanthollow.com
4.) Email: peterwalsh@verdanthollow.com
5.) My name: Peter Walsh
6.) Facebook link: facebook.com/VerdantHollowGrounds
7.) Instagram: http://instagram.com/verdanthollow

Attached is a copy of our logo.

```html
<!DOCTYPE html>
<html lang="en">
<head>
<meta charset="utf-8">
<title>Verdant Hollow – Business Card</title>
<link rel="stylesheet" href="https://fonts.googleapis.com/css2?family=Arimo:wght@700&display=swap">
<style>
  :root {
    --backdrop: #d9dde2;
    --card: #ffffff;
    --ink: #4a4a4a;
    --ink-dark: #2b2b2b;
    --accent: #e4602a;
  }
  * { margin: 0; padding: 0; box-sizing: border-box; }
  html, body {
    width: 1200px;
    height: 1000px;
    overflow: hidden;
    background: var(--backdrop);
  }
  .business-card {
    position: absolute;
    left: 100px;
    top: 214px;
    width: 1000px;
    height: 572px;
    background: var(--card);
    font-family: "Arimo", Arial, sans-serif;
    font-weight: 700;
    color: var(--ink);
    box-shadow: 0 10px 30px rgba(0, 0, 0, 0.12);
  }
  .brand {
    position: absolute;
    left: 70px;
    top: 330px;
    display: flex;
    align-items: center;
    gap: 16px;
  }
  .brand-dot {
    width: 44px;
    height: 44px;
    border-radius: 50%;
    background: var(--accent);
  }
  .brand-name {
    font-size: 32px;
    color: var(--ink-dark);
    letter-spacing: 0.5px;
  }
  .holder-name {
    position: absolute;
    right: 70px;
    top: 70px;
    font-size: 30px;
    color: var(--ink);
  }
  .contact-list {
    position: absolute;
    right: 70px;
    top: 250px;
    list-style: none;
    text-align: right;
    font-size: 21px;
    line-height: 37px;
  }
  .contact-list .gap { margin-top: 22px; }
</style>
</head>
<body>
  <div class="business-card">
    <div class="brand">
      <span class="brand-dot"></span>
      <span class="brand-name">Verdant Hollow</span>
    </div>
    <h1 class="holder-name">Peter Walsh</h1>
    <ul class="contact-list">
      <li>Phone : (816) 555-0193</li>
      <li>Email : peterwalsh@verdanthollow.com</li>
      <li>Website : Verdanthollow.com</li>
      <li class="gap">Instagram : http://instagram.com/verdanthollow</li>
      <li>Facebook : facebook.com/VerdantHollowGrounds</li>
    </ul>
  </div>
</body>
</html>
```